HR consultancy website - Wordpress Design Project

We need a wordpress design for a new company based in Belgium called Brivolane. We propose HR consultancy services focused on employees' engagement (motivation). We target corporations from 100 to 1000+ employees mainly in Europe.
We need a new design for our existing website (www.brivolane.eu).
We find the current design too static and outdated and we are looking for a more appealing look & feel.
Nevertheless, it has also to be sober.
The colours of the logo (dark blue, purple and light grey) should be preferrably used.
The content structure and the texts remain the same.

Target Market(s)

HR managers, general managers of SME's, higher education

Industry/Entity Type

It Company

Requirements
Must have
• No specific functionalities, except a contact form.

```html
<!DOCTYPE html>
<html lang="en">
<head>
<meta charset="utf-8">
<title>Brivolane – HR Engagement Consultancy</title>
<link href="https://fonts.googleapis.com/css2?family=Oswald:wght@400&family=Raleway:wght@300;400&family=Arimo:wght@400;700&display=swap" rel="stylesheet">
<style>
:root{
  --blue:#0b3f8e;
  --blue-dark:#072f6e;
  --pink:#d2266b;
  --taupe:#cdc4bd;
  --taupe-dark:#b9ada4;
  --grey-text:#4a4a4a;
  --light-line:#d6d6d6;
  --logo-grey:#cfc7bf;
  --nav-text:#3f3a36;
}
*{box-sizing:border-box;margin:0;padding:0}
html,body{width:1067px;height:1200px;overflow:hidden;background:#fff}
body{font-family:"Arimo",Arial,sans-serif;color:var(--grey-text);position:relative}
.abs{position:absolute}

/* top bar & nav */
.top-strip{left:0;top:0;width:1067px;height:4px;background:#d9d3cd}
.nav-home{left:132px;top:4px;width:42px;height:46px;background:var(--taupe-dark);border-radius:0 0 6px 6px;color:#fff}
.nav-item{top:20px;font-family:"Oswald",sans-serif;font-size:12.5px;color:var(--nav-text);letter-spacing:.2px}
.nav-home.nav-item{top:4px;padding-top:16px;text-align:center;color:#fff}
.search{left:775px;top:20px;width:126px;height:19px;border:1px solid #d5d5d5;background:#fff;font-size:9.5px;color:#888;padding:3px 6px}
.search-btn{right:0;top:0;width:17px;height:17px;background:#c7c2bd}

/* logo band */
.logo-band{left:0;top:68px;width:1067px;height:101px;background:linear-gradient(100deg,#f2f2f2 0%,#fafafa 45%,#f0f0f0 100%)}
.logo{left:131px;top:84px;font-family:"Arimo",Arial,sans-serif;font-size:60px;color:var(--logo-grey);letter-spacing:1px;line-height:1}

/* hero */
.hero{left:0;top:169px;width:1067px;height:331px;background:var(--taupe)}
.hero-photo{left:533px;top:169px;width:534px;height:331px;background:radial-gradient(ellipse at 65% 45%,#e9c9b2 0%,#c8a58f 30%,#bfb3aa 60%,var(--taupe) 100%)}
.welcome{left:201px;top:214px;font-family:"Raleway",sans-serif;font-weight:300;font-size:46px;color:var(--pink);letter-spacing:-1px}
.hero-link{left:208px;top:273px;font-size:12px;color:var(--blue);text-decoration:underline}
.hero-text{left:208px;top:292px;width:300px;font-family:"Arimo",Arial,sans-serif;font-size:11px;line-height:21.3px;color:#f5f2ef}
.btn-more{left:212px;top:411px;width:98px;height:32px;background:var(--blue);border-radius:10px;color:#fff;font-size:15px;text-align:center;line-height:32px;box-shadow:0 2px 3px rgba(0,0,0,.2)}
.pager{left:161px;top:470px;width:100px;height:20px;font-size:10px;color:var(--blue)}
.pager span{position:absolute;top:4px}
.pager .current{left:26px;top:0;width:18px;height:18px;border-radius:50%;background:#fff;text-align:center;line-height:18px}

/* features */
.feature{top:514px}
.feature h3{font-size:14px;font-weight:700;color:var(--pink);margin-top:11px}
.feature .num{position:absolute;right:0;top:0;font-family:"Raleway",sans-serif;font-size:32px;color:var(--pink);font-variant-numeric:lining-nums;line-height:1.1}
.feature p{margin-top:16px;width:161px;font-size:10.5px;line-height:16px;color:#2b2b2b;text-align:justify}
.feature-divider{top:510px;width:2px;height:150px;background:linear-gradient(#fff,#e4e4e4,#fff)}
.section-line{left:0;top:667px;width:1067px;height:1px;background:#e3e3e3}

/* middle */
.col-title{font-size:15px;font-weight:700;color:var(--pink)}
.col-rule{height:0;border-top:1px dashed #c9c9c9}
.small-text{font-size:10px;line-height:12.5px;color:#3a3a3a}
.social-tile{top:756px;width:44px;height:44px;border-radius:7px;box-shadow:0 2px 3px rgba(0,0,0,.25)}
.news-heading{font-family:"Raleway",sans-serif;font-size:16px;color:#333}
.field{border:1px solid #d4d4d4;border-radius:3px;background:#fff;font-size:10px;color:#aaa;padding:8px 12px;box-shadow:inset 0 1px 2px rgba(0,0,0,.06)}
.btn-arrow{height:28px;width:142px;background:linear-gradient(var(--blue),var(--blue-dark));border:1px solid #052758;color:#fff;font-size:11.5px;line-height:26px;padding-left:11px}
.btn-arrow svg{position:absolute;right:10px;top:11px}
.thumb{width:50px;height:50px;border:3px solid #fff;box-shadow:0 0 2px rgba(0,0,0,.35)}
.news-text{width:200px;font-size:10px;line-height:12.5px;color:#3a3a3a}
.news-sep{left:711px;width:178px;border-top:1px dashed #c9c9c9}

/* footer */
.footer-top{left:0;top:1004px;width:1067px;height:3px;background:#ececec}
.footer-divider{top:1007px;width:1px;height:128px;background:#ececec}
.foot-head{font-size:14px;color:#333}
.foot-link{font-size:10.5px;color:#444}
.foot-item{font-size:10.5px;color:#444}
.foot-item a,.member a{color:var(--blue);text-decoration:underline}
.foot-item svg,.member svg{position:absolute;left:-20px;top:0}
.pink-bar{left:0;top:1145px;width:1067px;height:5px;background:var(--pink)}
.copyright{left:142px;top:1160px;font-size:10px;color:#444}
.follow{left:787px;top:1164px;font-size:9.5px;color:#444}
.follow-tile{top:1162px;width:14px;height:14px;border-radius:2px}
</style>
</head>
<body>

<div class="abs top-strip"></div>
<div class="abs nav-home nav-item">HOME</div>
<div class="abs nav-item" style="left:210px">ABOUT US</div>
<div class="abs nav-item" style="left:285px">OUR MISSION</div>
<div class="abs nav-item" style="left:373px">SOLUTIONS</div>
<div class="abs nav-item" style="left:457px">CAREERS</div>
<div class="abs nav-item" style="left:542px">CONTACTS</div>
<div class="abs search">Search...
  <div class="abs search-btn">
    <svg width="17" height="17" viewBox="0 0 17 17"><circle cx="7.5" cy="7.5" r="3.5" fill="none" stroke="#fff" stroke-width="1.5"/><line x1="10" y1="10" x2="13" y2="13" stroke="#fff" stroke-width="1.6"/></svg>
  </div>
</div>

<div class="abs logo-band"></div>
<div class="abs logo">BRIVOLANE</div>

<div class="abs hero"></div>
<div class="abs hero-photo" role="img" aria-label="Photo of a smiling young woman giving a thumbs up, with colleagues blurred in the background"></div>
<div class="abs welcome">WELCOME!</div>
<div class="abs hero-link">Lorem ipsum dolor sit amet, consectetuer</div>
<div class="abs hero-text">Donec lobortis purus vel urna. Nunc laoreet lacinia nunc. In volutpat sodales ipsum. Sed vestibulum. Donec lobortis purus vel urna. Nunc laoreet lacinia nunc. In volutpat sodales ipsum. Sed vestibulum.</div>
<div class="abs btn-more">Read More</div>
<div class="abs pager">
  <svg class="abs" style="left:0;top:2px" width="24" height="16" viewBox="0 0 24 16"><path d="M8 1 L2 8 L8 15" fill="none" stroke="#b0a69e" stroke-width="3"/><path d="M14 1 L20 8 L14 15" fill="none" stroke="#b0a69e" stroke-width="3"/></svg>
  <span class="current">1</span>
  <span style="left:50px">2</span>
  <span style="left:71px">3</span>
</div>

<div class="abs feature" style="left:135px;width:175px"><h3>EVALUATION</h3><span class="num">01</span><p>Only between 13 and 21% of employees are actively engaged</p></div>
<div class="abs feature-divider" style="left:325px"></div>
<div class="abs feature" style="left:340px;width:174px"><h3>STRATEGY</h3><span class="num">02</span><p>Brivolane helps corporate leaders get the best contribution from employees.</p></div>
<div class="abs feature-divider" style="left:528px"></div>
<div class="abs feature" style="left:546px;width:174px"><h3>PROCESS</h3><span class="num">03</span><p>Our ERM tool creates an HR engagement cycle to encourage line managers to take initiatives and to enhance the engagement of their team members.</p></div>
<div class="abs feature-divider" style="left:733px"></div>
<div class="abs feature" style="left:755px;width:178px"><h3>IMPACT</h3><span class="num">04</span><p style="text-align:left">Our ERM tool measures impact by creating an index which can then be used for comparison over time.</p></div>
<div class="abs section-line"></div>

<!-- social / newsletter -->
<div class="abs col-title" style="left:133px;top:692px">Social Connection</div>
<div class="abs col-rule" style="left:133px;top:714px;width:258px"></div>
<div class="abs small-text" style="left:134px;top:725px;width:260px">At vero eos et accusamus et iusto odio dignissimos ducimus qui blanditiis praesentium</div>
<div class="abs social-tile" style="left:133px;background:#e85a22"></div>
<div class="abs social-tile" style="left:188px;background:#3b5ea0"></div>
<div class="abs social-tile" style="left:242px;background:#2f7bb5"></div>
<div class="abs social-tile" style="left:294px;background:#b8201f"></div>
<div class="abs social-tile" style="left:348px;background:#4fb7c6"></div>

<div class="abs news-heading" style="left:133px;top:833px">Newsletter</div>
<div class="abs col-rule" style="left:133px;top:856px;width:205px"></div>
<div class="abs small-text" style="left:134px;top:866px;width:260px">At vero eos et accusamus et iusto odio dignissimos ducimus qui blanditiis praesentium</div>
<div class="abs field" style="left:134px;top:901px;width:258px;height:29px">your email address</div>
<div class="abs btn-arrow" style="left:134px;top:940px">Subscribe<svg width="16" height="5" viewBox="0 0 16 5"><path d="M0 2.5 H14 M11 0 L14 2.5 L11 5" stroke="#fff" fill="none" stroke-width=".8" stroke-dasharray="1.5 1"/></svg></div>

<!-- contact form -->
<div class="abs col-title" style="left:408px;top:692px">Contact</div>
<div class="abs col-rule" style="left:408px;top:714px;width:258px"></div>
<div class="abs field" style="left:408px;top:729px;width:257px;height:28px">your name</div>
<div class="abs field" style="left:408px;top:772px;width:257px;height:28px">your email address</div>
<div class="abs field" style="left:408px;top:813px;width:257px;height:117px">message</div>
<div class="abs btn-arrow" style="left:411px;top:940px">Send it<svg width="16" height="5" viewBox="0 0 16 5"><path d="M0 2.5 H14 M11 0 L14 2.5 L11 5" stroke="#fff" fill="none" stroke-width=".8" stroke-dasharray="1.5 1"/></svg></div>

<!-- news -->
<div class="abs col-title" style="left:686px;top:692px">News Updates</div>
<div class="abs col-rule" style="left:686px;top:714px;width:257px"></div>
<div class="abs thumb" style="left:687px;top:729px;background:radial-gradient(circle,#f08a2a 0%,#d2532a 45%,#3a4f9a 80%)" role="img" aria-label="News thumbnail: browser graphic"></div>
<div class="abs news-text" style="left:743px;top:727px">Lorem ipsum dolor sit amet, consectetur adipisicing elit, sed do eiusmod tempor incididunt ut labore et dolore magna aliqua.</div>
<div class="abs news-sep" style="top:786px"></div>
<div class="abs thumb" style="left:687px;top:800px;background:radial-gradient(circle at 40% 40%,#ff5fd8 0%,#b0138f 35%,#2a0428 85%)" role="img" aria-label="News thumbnail: abstract magenta lights"></div>
<div class="abs news-text" style="left:743px;top:798px">Sed ut perspiciatis unde omnis iste natus error sit voluptatem accusantium dolor-emque laudantium, totam rem aperiam.</div>
<div class="abs news-sep" style="top:857px"></div>
<div class="abs thumb" style="left:687px;top:871px;background:linear-gradient(160deg,#6fc3df 0%,#3aa1c9 40%,#f3d53a 65%,#d0388e 100%)" role="img" aria-label="News thumbnail: colourful abstract waves"></div>
<div class="abs news-text" style="left:743px;top:869px">At vero eos et accusamus et iusto odio dignissimos ducimus qui blanditiis praesen-tium.</div>
<div class="abs news-sep" style="top:930px"></div>
<div class="abs btn-arrow" style="left:686px;top:940px">Visit our Blog<svg width="16" height="5" viewBox="0 0 16 5"><path d="M0 2.5 H14 M11 0 L14 2.5 L11 5" stroke="#fff" fill="none" stroke-width=".8" stroke-dasharray="1.5 1"/></svg></div>

<!-- footer -->
<div class="abs footer-top"></div>
<div class="abs footer-divider" style="left:412px"></div>
<div class="abs footer-divider" style="left:683px"></div>

<div class="abs foot-head" style="left:148px;top:1033px">Quick Links</div>
<div class="abs foot-link" style="left:149px;top:1062px">Home</div>
<div class="abs foot-link" style="left:149px;top:1078px">About</div>
<div class="abs foot-link" style="left:149px;top:1094px">Our Mission</div>
<div class="abs foot-link" style="left:256px;top:1062px">Solution</div>
<div class="abs foot-link" style="left:256px;top:1078px">Careers</div>
<div class="abs foot-link" style="left:256px;top:1094px">Contact Us</div>

<div class="abs foot-head" style="left:435px;top:1038px">Contact us</div>
<div class="abs foot-item" style="left:454px;top:1069px">
  <svg width="14" height="13" viewBox="0 0 14 13"><path d="M1 7 L7 1 L13 7" fill="none" stroke="#2f5fa8" stroke-width="1.6"/><rect x="3" y="6" width="8" height="7" fill="#6f93c9"/><rect x="6" y="9" width="2" height="4" fill="#fff"/></svg>
  27 Rue des Tilleuls Namur, 5000</div>
<div class="abs foot-item" style="left:454px;top:1085px">
  <svg width="14" height="13" viewBox="0 0 14 13"><rect x="3" y="0" width="8" height="13" rx="1.5" fill="#3a6fb8"/><rect x="4.5" y="2" width="5" height="6" fill="#cfe0f5"/></svg>
  1.800.555.01.27</div>
<div class="abs foot-item" style="left:454px;top:1101px">
  <svg width="15" height="12" viewBox="0 0 15 12"><rect x=".5" y="1.5" width="14" height="10" fill="#f6d88a" stroke="#c9a24a"/><path d="M.5 1.5 L7.5 7 L14.5 1.5" fill="none" stroke="#c9a24a"/></svg>
  <a>hello@brivolane.eu</a></div>

<div class="abs foot-head" style="left:706px;top:1038px">We are team</div>
<div class="abs foot-item member" style="left:724px;top:1069px">
  <svg width="14" height="13" viewBox="0 0 14 13"><circle cx="7" cy="4" r="3" fill="#8a6a4a"/><path d="M1 13 Q7 5 13 13Z" fill="#2d4d80"/></svg>
  <a>Arno Veltmar</a>, CEO</div>
<div class="abs foot-item member" style="left:724px;top:1085px">
  <svg width="14" height="13" viewBox="0 0 14 13"><circle cx="7" cy="4" r="3" fill="#8a6a4a"/><path d="M1 13 Q7 5 13 13Z" fill="#2d4d80"/></svg>
  <a>Ines Dorval</a>, Director</div>
<div class="abs foot-item member" style="left:724px;top:1101px">
  <svg width="14" height="13" viewBox="0 0 14 13"><circle cx="7" cy="4" r="3" fill="#8a6a4a"/><path d="M1 13 Q7 5 13 13Z" fill="#2d4d80"/></svg>
  <a>Pieter Kaal</a>, Developer</div>

<div class="abs pink-bar"></div>
<div class="abs copyright">© 2012.www.brivolane.eu</div>
<div class="abs follow">Follow us</div>
<div class="abs follow-tile" style="left:837px;background:#e8701f"></div>
<div class="abs follow-tile" style="left:855px;background:#3fa7d8"></div>
<div class="abs follow-tile" style="left:873px;background:#3b5ea0"></div>
<div class="abs follow-tile" style="left:891px;background:#e9e9e9"></div>
<div class="abs follow-tile" style="left:909px;background:#2f7bb5"></div>

</body>
</html>
```